Website for AV installation with booking system and e-commerce

Company: Corvexa
Tag Line: Audio Visual and Security System Installations
We need a website for an AV company based in Sydney Australia. We specialise in Audio Visual, CCTV (security cameras), and Data Cabling.
The purpose of the website is that customers book their installation online with a live booking system.
We are looking for the following:
- Creative and modern design
- easy to use - keep in mind that the user who will book will have little knowledge in technology.
- clean and organised
- colours to work in well with our logo we also like royal to navy blue, but we are open to other suggested what works well with our logo.
We want customers to be able to add products needed for their installation ie when booking to wall mount their TV they can choose to add a TV bracket and cables to the cart and vise-versa buy a bracket or cables and add to cart the installation.
Tabs to be included:
About us
Gallery
Contact Us
Home
Services (there are three services that we offer - Residential, Corporate and Retail)
Products
Book Online/Cart (checkout)
Temporary website checkout: www.corvexa.com.au, please note this is very basic and we do not want a copy of this. This is purely to give you an idea of our company.
Good Luck!
Target Market(s)
home owners/renters, business owners, archiects/designers, builders
Industry/Entity Type
E-Commerce
Look and feel

```html
<!DOCTYPE html>
<html lang="en">
<head>
<meta charset="utf-8">
<title>Corvexa – Audio Visual And Security System Installations</title>
<link href="https://fonts.googleapis.com/css2?family=Carlito:wght@400;700&family=Aldrich&display=swap" rel="stylesheet">
<style>
  :root{
    --red:#e10a0a;
    --red-dark:#b80000;
    --black:#000;
    --header-top:#2a2a2a;
    --header-bottom:#3c3c3c;
    --page-bg:#f2f2f2;
    --white:#fff;
    --text:#333;
    --muted:#555;
    --line:#bdbdbd;
    --card-head:#e6e6e6;
    --footer-top:#3a3a3a;
    --footer-bottom:#4a4a4a;
  }
  *{box-sizing:border-box;margin:0;padding:0}
  html,body{width:1200px;height:939px;overflow:hidden}
  body{position:relative;background:var(--page-bg);font-family:'Carlito',Calibri,sans-serif;color:var(--text)}
  .abs{position:absolute}

  .topbar{left:0;top:0;width:1200px;height:33px;background:var(--black)}
  .tagline{left:190px;top:5px;font-family:'Aldrich',sans-serif;font-size:17px;color:#cfcfcf;letter-spacing:.3px}
  .top-btn{top:0;height:33px;background:var(--red);color:var(--white);font-weight:700;font-size:15px;display:flex;align-items:center;gap:12px;padding-left:12px}
  .top-btn.booking{left:735px;width:139px}
  .top-btn.cart{left:879px;width:141px;padding-left:14px}

  .header{left:0;top:33px;width:1200px;height:94px;background:linear-gradient(var(--header-top),var(--header-bottom))}
  .brand{left:186px;top:52px;display:flex;align-items:center;gap:10px}
  .brand-dot{width:26px;height:26px;border-radius:50%;background:var(--red)}
  .brand-name{font-family:'Carlito',sans-serif;font-weight:700;font-size:40px;color:var(--white);line-height:1}
  .nav-band{left:465px;top:64px;width:735px;height:31px;background:var(--black)}
  .nav{left:465px;top:64px;height:31px;display:flex;align-items:center}
  .nav a{color:var(--white);text-decoration:none;font-weight:700;font-size:15px;letter-spacing:1.2px;text-transform:uppercase;position:absolute;top:7px;white-space:nowrap}
  .nav a.active{background:var(--red);top:0;height:31px;width:77px;padding-top:7px;text-align:center;left:0}

  .hero-band{left:0;top:127px;width:1200px;height:253px;background:var(--white);box-shadow:0 3px 4px rgba(0,0,0,.12)}
  .hero-frame{left:180px;top:134px;width:840px;height:241px;border:1px solid #d4d4d4;background:var(--white)}
  .hero-photo{left:185px;top:138px;width:830px;height:232px;background:linear-gradient(90deg,#6b4a33 0%,#a58c78 30%,#cfc2b4 55%,#8a6a48 80%,#6a7f98 100%)}

  .content{left:180px;top:381px;width:840px;height:489px;background:var(--white)}
  .welcome{left:185px;top:392px;width:602px;text-align:center;font-size:18px;font-weight:700;color:#222}
  .welcome span{color:var(--red)}
  .dash{left:185px;top:422px;width:602px;border-top:1px dashed var(--line)}
  .intro{left:190px;top:430px;width:598px;font-size:11.6px;line-height:19px;color:var(--muted)}
  .intro p+p{margin-top:9px}

  .login{left:802px;top:399px;width:203px;height:131px;background:var(--white);border:1px solid #ddd;border-bottom:4px solid #777;border-radius:3px 3px 0 0}
  .login-head{left:0;top:0;width:201px;height:24px;background:linear-gradient(var(--red),var(--red-dark));color:var(--white);font-weight:700;font-size:14px;text-align:center;line-height:24px;border-radius:3px 3px 0 0}
  .field{left:11px;width:180px;height:23px;border:1px solid #ccc;border-radius:4px;background:linear-gradient(#fff,#ececec);font-size:11.5px;color:#666;padding:4px 8px}
  .login-btn{left:12px;top:96px;width:82px;height:20px;border-radius:4px;background:linear-gradient(#666,#222);color:var(--white);font-size:11.5px;font-weight:700;padding-left:23px;line-height:20px}

  .sep{left:180px;top:541px;width:840px;height:3px;background:#ececec}
  .services-title{left:189px;top:550px;font-size:16px;font-weight:700;color:var(--red)}
  .services{left:187px;top:581px;width:827px;height:277px;border:3px dotted #777}
  .card{top:0;width:275px;height:271px}
  .card+.card{border-left:2px dotted #777}
  .card-head{left:8px;top:8px;width:258px;height:35px;background:var(--card-head);font-size:17px;font-weight:700;color:#444;padding:9px 13px}
  .plus{right:10px;top:7px;width:21px;height:21px;border-radius:50%;background:var(--red);border:2px solid #fff;box-shadow:0 0 0 1px #ccc}
  .plus::before,.plus::after{content:"";position:absolute;left:50%;top:50%;background:#fff;transform:translate(-50%,-50%)}
  .plus::before{width:9px;height:2px}
  .plus::after{width:2px;height:9px}
  .card-photo{left:8px;top:50px;width:258px;height:133px}
  .card-text{left:6px;top:192px;width:262px;text-align:center;font-size:11.2px;line-height:19px;color:var(--muted)}

  .footer{left:0;top:870px;width:1200px;height:69px;background:linear-gradient(var(--footer-top),var(--footer-bottom))}
  .foot-links{left:195px;top:881px;font-size:12.5px;color:var(--white);white-space:nowrap}
  .foot-links span{margin:0 9px}
  .copyright{left:364px;top:908px;font-size:11.5px;color:var(--white)}
  .social{top:887px;width:26px;height:26px;border-radius:50%;background:linear-gradient(#fff,#d9d9d9);border:1px solid #999}
</style>
</head>
<body>
  <div class="abs topbar"></div>
  <div class="abs tagline">Audio Visual And Security System Installations</div>
  <div class="abs top-btn booking">
    <svg width="19" height="16" viewBox="0 0 19 16"><rect x="1" y="2" width="17" height="13" fill="none" stroke="#fff" stroke-width="1.6"/><line x1="1" y1="6" x2="18" y2="6" stroke="#fff" stroke-width="1.6"/><rect x="5" y="8" width="3" height="3" fill="#fff"/><rect x="11" y="8" width="3" height="3" fill="#fff"/></svg>
    My Booking
  </div>
  <div class="abs top-btn cart">
    <svg width="22" height="18" viewBox="0 0 22 18"><path d="M1 2h4l3 10h10l3-7H7" fill="none" stroke="#fff" stroke-width="2"/><circle cx="9" cy="15.5" r="1.8" fill="#fff"/><circle cx="17" cy="15.5" r="1.8" fill="#fff"/></svg>
    Cart (0.00)
  </div>

  <div class="abs header"></div>
  <div class="abs brand"><span class="brand-dot"></span><span class="brand-name">Corvexa</span></div>
  <div class="abs nav-band"></div>
  <nav class="abs nav">
    <a class="active" href="#">Home</a>
    <a href="#" style="left:94px">About Us</a>
    <a href="#" style="left:198px">Gallery</a>
    <a href="#" style="left:288px">Services</a>
    <a href="#" style="left:380px">Product</a>
    <a href="#" style="left:474px">Contact</a>
  </nav>

  <div class="abs hero-band"></div>
  <div class="abs hero-frame"></div>
  <div class="abs hero-photo" role="img" aria-label="Banner photo: wooden speaker on a desk beside a laptop, and a woman listening to earphones outdoors"></div>

  <div class="abs content"></div>
  <h1 class="abs welcome">Welcome <span>to Corvexa</span></h1>
  <div class="abs dash"></div>
  <div class="abs intro">
    <p>Lorem Ipsum is simply dummy text of the printing and typesetting industry. Lorem Ipsum has been the industry's standard dummy text ever since the 1500s, when an unknown printer took a galley of type and scrambled it to make a type specimen book. It has survived not only five centuries, but also the leap into electronic typesetting, remaining essentially unchanged.</p>
    <p>It was popularised in the 1960s with the release of Typeline sheets containing Lorem Ipsum passages, and more recently<br>with desktop publishing software like Pressform Layout including versions of Lorem Ipsum.</p>
  </div>

  <div class="abs login">
    <div class="abs login-head">Login</div>
    <div class="abs field" style="top:33px">Username :</div>
    <div class="abs field" style="top:63px">Password :</div>
    <div class="abs login-btn">Login</div>
  </div>

  <div class="abs sep"></div>
  <h2 class="abs services-title">» Services</h2>
  <div class="abs services">
    <div class="abs card" style="left:0">
      <div class="abs card-head">Residential<span class="abs plus"></span></div>
      <div class="abs card-photo" role="img" aria-label="Photo of a living room with a wall-mounted TV and speakers" style="background:linear-gradient(90deg,#3f5868,#4a2a2a 35%,#5a3030 65%,#8a9aa8)"></div>
      <p class="abs card-text">Lorem Ipsum is simply dummy text of the printing<br>and typespecimen book. It has survived not only five centuries, but also the leap into electronic<br>typesetting, rtially unchanged.</p>
    </div>
    <div class="abs card" style="left:275px">
      <div class="abs card-head">Corporate<span class="abs plus"></span></div>
      <div class="abs card-photo" role="img" aria-label="Photo of a conference hall with projection screens" style="background:linear-gradient(#7a5a20,#3a2a14 40%,#4a3a28 70%,#2a1a10)"></div>
      <p class="abs card-text">Lorem Ipsum is simply dummy text of the printing<br>and typespecimen book. It has survived not only five centuries, but also the leap into electronic<br>typesetting, rtially unchanged.</p>
    </div>
    <div class="abs card" style="left:550px">
      <div class="abs card-head">Retail<span class="abs plus"></span></div>
      <div class="abs card-photo" role="img" aria-label="Photo of an event stage with blue lighting and screens" style="background:linear-gradient(#1a2a6a,#3a5ab0 45%,#2a3a8a 70%,#101840)"></div>
      <p class="abs card-text">Lorem Ipsum is simply dummy text of the printing<br>and typespecimen book. It has survived not only five centuries, but also the leap into electronic<br>typesetting, rtially unchanged.</p>
    </div>
  </div>

  <footer class="abs footer"></footer>
  <div class="abs foot-links">Home<span>|</span>About<span>|</span>Services<span>|</span>Gallery<span>|</span>Product<span>|</span>Contact Us<span>|</span>Privacy Policy<span>|</span>Terms &amp; Conditions</div>
  <div class="abs copyright">© Copyright 2013 By Corvexa. All Rights Reserved</div>
  <div class="abs social" style="left:918px"></div>
  <div class="abs social" style="left:951px"></div>
  <div class="abs social" style="left:985px"></div>
</body>
</html>
```